Hollowbrook Leasing Business Card Design

Need business cards designed for our new equipment rental. We specialize in renting to landscape / tree professionals, contractors, Do-It-Yourself'ers and Around the home or office. Looking for a eye catching card. Landscape and construction should be the theme. The logo is attached, and you can see our colors from the logo. You can use whatever color goes with it ok.

Target Market(s)

First off Landscape and Tree Professional. Then contractors, Do-It-Yourself'ers and rentals for Around the home or office.

Industry/Entity Type

Business

Contact Information for Business Card

Eye catching background that blends landscaping with construction equipment

Requirements
Must have
• Name on Card will Be: Derek Tollund (Manager)
• My Direct Phone Number is: 352-715-3092
• derek@hollowbrookleasing.example
• www.hollowbrookleasing.example
• 4172 Marsh Wren Lane,
• Dade City FL 33519
Nice to have
• Would be Nice to have these bullets on the Face of the card that does not have all my information.
• Serving:
• Landscape / Tree Professionals
• Contractors
• DYI'ers or say Do-It-Yourself'ers
• Maybe have serving small and centered above these bullets, and these 3 bullets along the bottom of the card. Ideas?

```html
<!DOCTYPE html>
<html lang="en">
<head>
<meta charset="utf-8">
<title>Hollowbrook Leasing – Business Card</title>
<link href="https://fonts.googleapis.com/css2?family=Work+Sans:wght@400;500;700&display=swap" rel="stylesheet">
<style>
  :root {
    --backdrop: #3a3230;
    --card-dark: #1f1f20;
    --card-light: #ffffff;
    --brand-blue: #1f4e86;
    --navy: #163a66;
    --steel: #a9acb0;
    --amber: #f2b04a;
    --ink: #3c3f44;
  }
  * { box-sizing: border-box; margin: 0; padding: 0; }
  html, body {
    width: 1200px; height: 715px; overflow: hidden;
    background: var(--backdrop);
    font-family: "Work Sans", Arial, sans-serif;
  }
  .sheet {
    width: 1200px; height: 715px;
    display: flex; align-items: center; justify-content: center; gap: 48px;
  }
  .card {
    width: 525px; height: 300px;
    border-radius: 4px;
    box-shadow: 0 12px 28px rgba(0,0,0,.45);
    position: relative;
  }
  .card--front {
    background: var(--card-dark);
    display: flex; align-items: center; justify-content: center;
    border-bottom: 4px solid var(--brand-blue);
  }
  .brand {
    display: flex; align-items: center; gap: 12px;
    font-weight: 700; letter-spacing: .02em;
  }
  .brand__dot {
    width: 16px; height: 16px; border-radius: 50%;
  }
  .card--front .brand { font-size: 34px; color: var(--steel); }
  .card--front .brand__dot { background: var(--amber); }

  .card--back {
    background: var(--card-light);
    display: flex; align-items: center;
    padding: 0 30px;
  }
  .card--back .brand {
    width: 205px; font-size: 21px; color: var(--brand-blue);
    line-height: 1.15;
  }
  .card--back .brand__dot { background: var(--amber); flex: none; width: 12px; height: 12px; }
  .divider {
    width: 2px; height: 136px; background: var(--brand-blue);
    margin: 0 22px 0 10px;
  }
  .contact { color: var(--ink); font-size: 13px; line-height: 1.45; }
  .contact__name {
    font-size: 21px; font-weight: 700; color: var(--navy);
    letter-spacing: .04em; text-transform: uppercase; line-height: 1.1;
  }
  .contact__title { margin-bottom: 4px; }
  .contact__row { display: flex; align-items: center; gap: 8px; }
  .contact__row svg { width: 10px; height: 10px; fill: var(--brand-blue); flex: none; }
  .contact__web strong { color: var(--brand-blue); font-weight: 500; }
</style>
</head>
<body>
<main class="sheet">
  <section class="card card--front" aria-label="Card front">
    <div class="brand"><span class="brand__dot"></span>Hollowbrook Leasing</div>
  </section>

  <section class="card card--back" aria-label="Card back">
    <div class="brand"><span class="brand__dot"></span>Hollowbrook Leasing</div>
    <div class="divider"></div>
    <div class="contact">
      <p class="contact__name">Derek Tollund</p>
      <p class="contact__title">Managing Director</p>
      <p>4172 Marsh Wren Lane,<br>Dade City, FL 33519</p>
      <p class="contact__row">
        <svg viewBox="0 0 10 10"><rect x="2.5" y="0" width="5" height="10" rx="1"/></svg>352-715-3092
      </p>
      <p class="contact__row">
        <svg viewBox="0 0 10 10"><path d="M2 0l2 2-1 1.5c.8 1.5 2 2.7 3.5 3.5L8 6l2 2-1.5 2C4 9.5.5 6 0 1.5z"/></svg>352-715-3093
      </p>
      <p class="contact__row">
        <svg viewBox="0 0 10 10"><path d="M0 2h10v6H0zM0 2l5 3.5L10 2" stroke="#fff" stroke-width=".8"/></svg>derek@hollowbrookleasing.example
      </p>
      <p class="contact__row contact__web">
        <svg viewBox="0 0 10 10"><circle cx="5" cy="5" r="4.5"/><path d="M.5 5h9M5 .5v9" stroke="#fff" stroke-width=".7"/></svg>www.<strong>hollowbrookleasing</strong>.example
      </p>
    </div>
  </section>
</main>
</body>
</html>
```